Shipping Box & Supplies - Aquatics

Design shipping boxes and padded envelopes

Target Market(s)

Local Consumers

Industry/Entity Type

Tropical Fish/Aquatics

Requirements
Must have
• Logo, website and national telephone number
Nice to have
• Pictures attached
Should not have
• address

```html
<!DOCTYPE html>
<html lang="en">
<head>
<meta charset="utf-8">
<title>Reefline Aquatics – Shipping Box Dieline</title>
<link rel="stylesheet" href="https://fonts.googleapis.com/css2?family=Michroma&family=Saira+Condensed:wght@600;700&display=swap">
<style>
  :root {
    --paper: #ffffff;
    --box-blue: #2b67a5;
    --box-blue-deep: #245a93;
    --box-teal: #16a89c;
    --box-orange: #f28a1e;
    --ink-navy: #2a2874;
    --ink-white: #ffffff;
    --seaweed: #3dbf9e;
    --cut-line: #c2445a;
  }
  html, body { margin: 0; padding: 0; overflow: hidden; background: var(--paper); }
  .canvas { width: 766px; height: 1200px; position: relative; overflow: hidden; background: var(--paper); }
  .canvas svg { display: block; }
  .brand-name { font-family: "Michroma", sans-serif; }
  .brand-sub { font-family: "Michroma", sans-serif; }
  .caution, .phone, .web { font-family: "Saira Condensed", sans-serif; font-weight: 700; }
  .panel-blue { fill: var(--box-blue); }
  .panel-teal { fill: var(--box-teal); }
  .panel-orange { fill: var(--box-orange); }
  .cut { stroke: var(--cut-line); stroke-width: 0.5; }
  .fold { stroke: var(--cut-line); stroke-width: 0.4; opacity: 0.6; fill: none; }
  .on-blue { color: var(--ink-white); }
  .on-light { color: var(--ink-navy); }
  .pattern-fill { fill: url(#sea-pattern); }
  .seabed-fill { fill: url(#seabed); }
  .icon-box { fill: none; stroke: currentColor; stroke-width: 0.8; }
  .icon-mark { fill: none; stroke: currentColor; stroke-width: 0.8; stroke-linecap: round; }
</style>
</head>
<body>
<div class="canvas">
<svg width="766" height="1200" viewBox="0 0 766 1200" xmlns="http://www.w3.org/2000/svg">
  <defs>
    <linearGradient id="sea-pattern" x1="0" y1="0" x2="1" y2="1">
      <stop offset="0" stop-color="#7fd6c4" stop-opacity="0.10"/>
      <stop offset="0.5" stop-color="#7fd6c4" stop-opacity="0.18"/>
      <stop offset="1" stop-color="#7fd6c4" stop-opacity="0.10"/>
    </linearGradient>
    <linearGradient id="seabed" x1="0" y1="0" x2="0" y2="1">
      <stop offset="0" stop-color="#3dbf9e" stop-opacity="0"/>
      <stop offset="1" stop-color="#3dbf9e" stop-opacity="0.45"/>
    </linearGradient>

    <symbol id="up-arrow" viewBox="0 0 8 16">
      <path d="M4 0 L8 6 H5.5 V16 H2.5 V6 H0 Z" fill="#ffffff"/>
    </symbol>

    <!-- Front face: brand name, caution line, web and phone -->
    <symbol id="front-face" viewBox="0 0 202 202">
      <rect class="pattern-fill" x="0" y="0" width="202" height="202" role="img" aria-label="Faint line drawings of tropical fish scattered across the panel"/>
      <rect class="seabed-fill" x="0" y="168" width="202" height="34" role="img" aria-label="Line drawings of coral, shells and seaweed along the bottom edge"/>
      <use href="#up-arrow" x="8" y="4" width="8" height="16"/>
      <use href="#up-arrow" x="186" y="4" width="8" height="16"/>
      <text class="brand-name" x="101" y="86" text-anchor="middle" font-size="23" fill="currentColor">REEFLINE</text>
      <text class="brand-sub" x="101" y="120" text-anchor="middle" font-size="15" letter-spacing="7" fill="currentColor">AQUATICS</text>
      <text class="caution" x="101" y="142" text-anchor="middle" font-size="7.5" letter-spacing="0.9" fill="currentColor">CAUTION: DELICATE AQUATIC CONTENTS</text>
      <text class="web" x="6" y="197" font-size="6" letter-spacing="0.4" fill="currentColor">www.reeflineaquatics.com</text>
      <text class="phone" x="196" y="197" text-anchor="end" font-size="6" letter-spacing="0.4" fill="currentColor">555-014-7730</text>
    </symbol>

    <!-- Side face: small brand, handling icons, contact -->
    <symbol id="side-face" viewBox="0 0 148 202">
      <rect class="pattern-fill" x="0" y="0" width="148" height="202" role="img" aria-label="Faint line drawings of tropical fish scattered across the panel"/>
      <rect class="seabed-fill" x="0" y="168" width="148" height="34" role="img" aria-label="Line drawings of coral, shells and seaweed along the bottom edge"/>
      <use href="#up-arrow" x="6" y="4" width="8" height="16"/>
      <use href="#up-arrow" x="134" y="4" width="8" height="16"/>
      <text class="brand-name" x="74" y="80" text-anchor="middle" font-size="9" fill="currentColor">REEFLINE</text>
      <text class="brand-sub" x="74" y="88" text-anchor="middle" font-size="4" letter-spacing="2" fill="currentColor">AQUATICS</text>
      <g class="handling-icons">
        <rect class="icon-box" x="46" y="100" width="16" height="16"/>
        <path class="icon-mark" d="M50 103 H58 L56 108 H52 Z M54 108 V113 M51 113 H57"/>
        <rect class="icon-box" x="66" y="100" width="16" height="16"/>
        <path class="icon-mark" d="M70 104 L78 112 M78 104 L70 112"/>
        <rect class="icon-box" x="86" y="100" width="16" height="16"/>
        <path class="icon-mark" d="M88 108 A6 5 0 0 1 100 108 Z M94 108 V113 Q94 114.5 92.5 114"/>
        <rect class="icon-box" x="46" y="119" width="16" height="16"/>
        <path class="icon-mark" d="M50 124 H58 V131 H50 Z M48 128 L50 132 M60 128 L58 132"/>
        <rect class="icon-box" x="66" y="119" width="16" height="16"/>
        <path class="icon-mark" d="M74 121 V126 M72 124 L74 126 L76 124 M70 127 H78 V133 H70 Z"/>
        <rect class="icon-box" x="86" y="119" width="16" height="16"/>
        <path class="icon-mark" d="M94 121.5 L98 128 H90 Z"/>
      </g>
      <text class="phone" x="74" y="150" text-anchor="middle" font-size="7" letter-spacing="0.4" fill="currentColor">555-014-7730</text>
      <text class="web" x="74" y="157" text-anchor="middle" font-size="4.5" fill="currentColor">www.reeflineaquatics.com</text>
    </symbol>

    <!-- Lid: centred small brand with contact -->
    <symbol id="lid-face" viewBox="0 0 200 120">
      <text class="brand-name" x="100" y="56" text-anchor="middle" font-size="11" fill="currentColor">REEFLINE</text>
      <text class="brand-sub" x="100" y="66" text-anchor="middle" font-size="5" letter-spacing="2.6" fill="currentColor">AQUATICS</text>
      <text class="phone" x="100" y="76" text-anchor="middle" font-size="6.5" letter-spacing="0.4" fill="currentColor">555-014-7730</text>
      <text class="web" x="100" y="83" text-anchor="middle" font-size="4.5" fill="currentColor">www.reeflineaquatics.com</text>
    </symbol>
  </defs>

  <!-- Colour range: front faces flat -->
  <g class="colour-range">
    <g class="variant variant-teal">
      <rect class="panel-teal" x="24" y="60" width="220" height="220"/>
      <use href="#front-face" class="on-light" x="24" y="60" width="220" height="220"/>
    </g>
    <g class="variant variant-orange">
      <rect class="panel-orange" x="273" y="60" width="220" height="220"/>
      <use href="#front-face" class="on-light" x="273" y="60" width="220" height="220"/>
    </g>
    <g class="variant variant-blue">
      <rect class="panel-blue" x="522" y="60" width="220" height="220"/>
      <use href="#front-face" class="on-blue" x="522" y="60" width="220" height="220"/>
    </g>
    <g class="variant-side">
      <rect class="panel-blue" x="309" y="330" width="148" height="202"/>
      <use href="#side-face" class="on-blue" x="309" y="330" width="148" height="202"/>
    </g>
  </g>

  <!-- Dieline -->
  <g class="dieline">
    <polygon class="panel-blue cut" points="22,810 50,800 50,1002 22,992"/>

    <path class="panel-blue cut" d="M266 705 H394 V790 Q394 800 400 800 H252 Q262 790 262 770 Q262 745 266 735 Z"/>
    <path class="panel-blue cut" d="M400 800 V652 Q400 622 430 622 H570 Q600 622 600 652 V800 Z"/>
    <path class="panel-blue cut" d="M606 705 H734 V735 Q738 745 738 770 Q738 790 748 800 H602 Q606 795 606 790 Z"/>

    <path class="panel-blue cut" d="M252 1002 H400 Q394 1005 394 1012 V1098 H266 V1068 Q262 1058 262 1032 Q262 1012 252 1002 Z"/>
    <path class="panel-blue cut" d="M400 1002 H600 V1150 Q600 1180 570 1180 H430 Q400 1180 400 1150 Z"/>
    <path class="panel-blue cut" d="M602 1002 H748 Q738 1012 738 1032 Q738 1058 734 1068 V1098 H606 V1012 Q606 1005 602 1002 Z"/>

    <rect class="panel-blue" x="50" y="800" width="698" height="202"/>
    <rect class="pattern-fill" x="400" y="622" width="200" height="178" role="img" aria-label="Faint line drawings of tropical fish on the lid"/>
    <rect class="pattern-fill" x="400" y="1002" width="200" height="178" role="img" aria-label="Faint line drawings of tropical fish on the base"/>

    <use href="#front-face" class="on-blue" x="50" y="800" width="202" height="202"/>
    <use href="#side-face" class="on-blue" x="252" y="800" width="148" height="202"/>
    <use href="#front-face" class="on-blue" x="400" y="800" width="202" height="202"/>
    <use href="#side-face" class="on-blue" x="602" y="800" width="146" height="202"/>

    <use href="#lid-face" class="on-blue" x="400" y="650" width="200" height="120" transform="rotate(180 500 710)"/>
    <use href="#lid-face" class="on-blue" x="400" y="1030" width="200" height="120"/>

    <path class="fold" d="M50 800 H748 M50 1002 H748 M252 800 V1002 M400 622 V1180 M600 622 V1180 M400 652 H600 M400 1150 H600"/>
  </g>
</svg>
</div>
</body>
</html>
```